Business Card Design

We are a commercial real estate brokerage in San Francisco, leasing office buildings downtown.
I would like a clean, elegant look. Simple but powerful .

Industry/Entity Type

Business

Contact Information for Business Card

Colin Farrow
lic# 07281549
415.555.0172
colin@tarvo-commercial.example
tarvo-commercial.example

```html
<!DOCTYPE html>
<html lang="en">
<head>
<meta charset="utf-8">
<title>Tarvo Commercial – Business Card</title>
<link rel="stylesheet" href="https://fonts.googleapis.com/css2?family=Open+Sans:wght@300;400;600;700&display=swap">
<style>
  :root {
    --page-bg: #eceae6;
    --card-white: #ffffff;
    --panel-grey: #d6dbe3;
    --panel-slate: #6e7f99;
    --panel-slate-deep: #5f7089;
    --rule-dark: #2f2f2f;
    --brand-slate: #6e7f99;
    --text-dark: #222222;
    --text-mid: #555555;
    --text-light: #ffffff;
  }
  * { margin: 0; padding: 0; box-sizing: border-box; }
  html, body {
    width: 1200px; height: 806px; overflow: hidden;
    background: var(--page-bg);
    font-family: "Open Sans", Arial, sans-serif;
  }
  .card {
    position: absolute; left: 60px; top: 85px;
    width: 1080px; height: 636px;
    background: var(--card-white);
    box-shadow: 0 4px 18px rgba(0,0,0,0.18);
    overflow: hidden;
  }
  .logo-panel {
    position: absolute; left: 0; top: 0;
    width: 403px; height: 221px;
    background: var(--panel-grey);
  }
  .divider {
    position: absolute; left: 403px; width: 4px;
    background: var(--rule-dark);
  }
  .divider--top { top: 0; height: 221px; }
  .divider--bottom { top: 279px; height: 357px; }
  .contact-panel {
    position: absolute; left: 409px; top: 279px;
    width: 671px; height: 357px;
    background: var(--panel-slate);
  }
  .skyline-art {
    position: absolute; left: 0; bottom: 0;
    width: 100%; height: 260px;
    background: linear-gradient(to bottom, rgba(95,112,137,0) 0%, var(--panel-slate-deep) 60%, #5a6a82 100%);
  }
  .brand {
    position: absolute; left: 428px; top: 40px;
    color: var(--brand-slate); font-weight: 600;
    line-height: 1;
  }
  .brand__name { display: block; font-size: 114px; letter-spacing: -1px; }
  .brand__descriptor { display: block; font-size: 38px; letter-spacing: 1px; margin-top: 6px; }
  .website {
    position: absolute; left: 432px; top: 222px;
    font-size: 27px; font-weight: 700; color: var(--text-mid);
  }
  .agent {
    position: absolute; right: 714px; top: 380px;
    text-align: right;
  }
  .agent__name { font-size: 34px; font-weight: 600; color: var(--text-dark); line-height: 1.2; }
  .agent__licence { font-size: 27px; font-weight: 300; color: var(--text-dark); margin-top: 4px; }
  .contact-list {
    position: absolute; left: 440px; top: 392px;
    list-style: none; color: var(--text-light);
    font-size: 27px; font-weight: 600;
  }
  .contact-list__item { display: flex; align-items: center; height: 42px; }
  .contact-list__icon { width: 30px; height: 30px; margin-right: 14px; flex: none; }
</style>
</head>
<body>
  <main class="card">
    <div class="logo-panel"></div>
    <div class="divider divider--top"></div>
    <div class="divider divider--bottom"></div>

    <div class="contact-panel">
      <div class="skyline-art" role="img" aria-label="Faint downtown office skyline illustration"></div>
    </div>

    <div class="brand">
      <span class="brand__name">TARVO</span>
      <span class="brand__descriptor">COMMERCIAL</span>
    </div>
    <p class="website">tarvo-commercial.example</p>

    <div class="agent">
      <p class="agent__name">Colin Farrow</p>
      <p class="agent__licence">Lic Nr. 07281549</p>
    </div>

    <ul class="contact-list">
      <li class="contact-list__item">
        <svg class="contact-list__icon" viewBox="0 0 30 30" aria-hidden="true">
          <rect x="8" y="2" width="14" height="26" rx="3" fill="none" stroke="#fff" stroke-width="2.4"/>
          <line x1="12" y1="23" x2="18" y2="23" stroke="#fff" stroke-width="2"/>
        </svg>
        415.555.0172
      </li>
      <li class="contact-list__item">
        <svg class="contact-list__icon" viewBox="0 0 30 30" aria-hidden="true">
          <rect x="2" y="7" width="26" height="17" fill="none" stroke="#fff" stroke-width="2.2"/>
          <polyline points="2,7 15,17 28,7" fill="none" stroke="#fff" stroke-width="2.2"/>
        </svg>
        colin@tarvo-commercial.example
      </li>
    </ul>
  </main>
</body>
</html>
```